Create for us a Shop-Stopper Business Card

We need a standout, first class business card to go along with our new brand strategy. Sleek, Contemporary and fresh.

Colors and theme must sync with our websitewww.pelvorpower.co.uk

We want a business card that has a global brand appeal. TKR Energy is a small UK renewable company that specialises in energy projects in Africa. We want a business card that has the following characteristics: Very short, precise, global, stand out, NOT TOO LOUD but contemporary. The company's colour themes are White, Grey with a hint of green.

Target Market(s)

Business exec, high net worth individuals, investors, commercial leaders, suppliers, government officials

Industry/Entity Type

Solar Energy

Contact Information for Business Card

Logo, Name, Title, Address, web address, email,

Requirements
Must have
• Logo must be sharp
Nice to have
• Adapt fonts from the logo. The large circular side of the logo at the back in a very refreshing way
Should not have
• No solar panel shapes or image.Very little black. If possible avoid black. Its not coming out nice. I think !!!

```html
<!DOCTYPE html>
<html lang="en">
<head>
<meta charset="utf-8">
<title>TKR Energy – Business Card</title>
<link href="https://fonts.googleapis.com/css2?family=Open+Sans:wght@400;600;700&display=swap" rel="stylesheet">
<style>
  :root {
    --stage: #e9e9e6;
    --card-white: #ffffff;
    --ink: #3a3a3a;
    --ink-soft: #4a4a4a;
    --green: #1f7a34;
    --green-deep: #17692b;
    --green-light: #8cc34f;
    --band-grey: #555555;
    --rule: #cfcfcf;
  }
  * { margin: 0; padding: 0; box-sizing: border-box; }
  html, body { width: 1200px; height: 1000px; overflow: hidden; }
  body {
    background: var(--stage);
    font-family: "Open Sans", Arial, sans-serif;
    position: relative;
  }
  .card {
    position: absolute;
    left: 265px;
    width: 666px;
    height: 397px;
    overflow: hidden;
    box-shadow: 0 4px 14px rgba(0,0,0,.18);
  }
  /* Front */
  .card-front { top: 73px; background: var(--card-white); }
  .brand {
    position: absolute;
    display: flex;
    align-items: center;
    gap: 14px;
  }
  .brand-mark { border-radius: 50%; flex: none; }
  .brand-name { font-weight: 600; letter-spacing: 1px; white-space: nowrap; }
  .card-front .brand { left: 32px; top: 64px; }
  .card-front .brand-mark { width: 62px; height: 62px; border: 7px solid var(--green); }
  .card-front .brand-name { font-size: 38px; color: var(--ink); }

  .person { position: absolute; right: 32px; top: 194px; text-align: right; }
  .person-name { font-size: 20px; font-weight: 700; color: var(--green); letter-spacing: .5px; line-height: 26px; }
  .person-title { font-size: 16px; color: var(--ink-soft); line-height: 22px; }

  .divider { position: absolute; left: 180px; right: 32px; top: 256px; height: 1px; background: var(--rule); }

  .contact-list { position: absolute; left: 34px; top: 246px; list-style: none; }
  .contact-list li {
    display: flex; align-items: center; gap: 6px;
    font-size: 16px; color: var(--ink); line-height: 24.5px;
  }
  .contact-list svg { width: 14px; height: 14px; fill: var(--green); flex: none; }

  .address {
    position: absolute; right: 32px; top: 284px;
    text-align: right; font-size: 16px; color: var(--ink); line-height: 21px;
  }
  .front-band { position: absolute; left: 0; bottom: 0; width: 666px; height: 26px; }

  /* Back */
  .card-back {
    top: 532px;
    background: radial-gradient(ellipse 60% 70% at 50% 48%, var(--green-light) 0%, #4c9d3f 45%, var(--green) 80%, var(--green-deep) 100%);
  }
  .world-map {
    position: absolute; left: 60px; top: 38px; width: 580px; height: 250px;
    background: radial-gradient(ellipse at 50% 50%, rgba(40,120,50,.35), rgba(40,120,50,0) 70%);
  }
  .card-back .brand { left: 130px; top: 158px; }
  .card-back .brand-mark { width: 76px; height: 76px; border: 8px solid var(--card-white); }
  .card-back .brand-name { font-size: 46px; color: var(--card-white); }
  .back-web {
    position: absolute; left: 0; right: 0; top: 347px;
    text-align: center; font-size: 16px; color: var(--card-white);
  }
</style>
</head>
<body>

<section class="card card-front" aria-label="Business card front">
  <div class="brand">
    <span class="brand-mark"></span>
    <span class="brand-name">TKR ENERGY</span>
  </div>

  <div class="person">
    <p class="person-name">DANIEL HARWOOD</p>
    <p class="person-title">Managing Director</p>
  </div>

  <div class="divider"></div>

  <ul class="contact-list">
    <li><svg viewBox="0 0 14 14" aria-hidden="true"><path d="M4 0h6a1 1 0 0 1 1 1v12a1 1 0 0 1-1 1H4a1 1 0 0 1-1-1V1a1 1 0 0 1 1-1zm.5 2v8h5V2zm2.5 9a.9.9 0 1 0 0 1.8.9.9 0 0 0 0-1.8z"/></svg>+ 000 000 0000</li>
    <li><svg viewBox="0 0 14 14" aria-hidden="true"><path d="M1 4c2-3 10-3 12 0l-1 2-3-1V4H5v1L2 6zm2 3h8l1 5H2z"/></svg>+ 000 000 0000</li>
    <li><svg viewBox="0 0 14 14" aria-hidden="true"><path d="M0 3h14v1L7 8 0 4zm0 2.5 7 4 7-4V11H0z"/></svg>info@pelvorpower.co.uk</li>
    <li><svg viewBox="0 0 14 14" aria-hidden="true"><path d="M7 0a7 7 0 1 0 0 14A7 7 0 0 0 7 0zm0 1.5a5.5 5.5 0 0 1 4.8 2.8H9.5L8 2.5 6 4l1 2-2 1-2-2-1.3.5A5.5 5.5 0 0 1 7 1.5zM2 8l2 1 1 3a5.5 5.5 0 0 1-3-4zm6 4 1-3 3-1a5.5 5.5 0 0 1-4 4z"/></svg>www.ashlinepower.com</li>
  </ul>

  <p class="address">Level 18, 4 Marlow House<br>Leeds, 12, West Yorkshire</p>

  <svg class="front-band" viewBox="0 0 666 26" preserveAspectRatio="none" aria-hidden="true">
    <defs>
      <linearGradient id="greyBand" x1="0" x2="1">
        <stop offset="0" stop-color="#3f3f3f"/><stop offset="1" stop-color="#6a6a6a"/>
      </linearGradient>
      <linearGradient id="greenBand" x1="0" x2="1">
        <stop offset="0" stop-color="#7cb94a"/><stop offset="1" stop-color="#3f9a3c"/>
      </linearGradient>
    </defs>
    <polygon points="0,0 358,0 332,26 0,26" fill="url(#greyBand)"/>
    <polygon points="370,0 666,0 666,26 344,26" fill="url(#greenBand)"/>
  </svg>
</section>

<section class="card card-back" aria-label="Business card back">
  <div class="world-map" role="img" aria-label="Dotted world map in soft green"></div>
  <div class="brand">
    <span class="brand-mark"></span>
    <span class="brand-name">TKR ENERGY</span>
  </div>
  <p class="back-web">www.pelvorpower.co.uk</p>
</section>

</body>
</html>
```